Providing Back Office Solutions to Financial Advisors and Attorney Needs a Business Card Design

Need a Business Card Design that speaks to Financial Advisor and Attorneys. Some of the word that come to mind is Clean/Simple & Futuristic.

Industry/Entity Type

Business

```html
<!DOCTYPE html>
<html lang="en">
<head>
<meta charset="utf-8">
<title>Calvora Back Office Solutions – Business Card</title>
<link rel="stylesheet" href="https://fonts.googleapis.com/css2?family=Roboto:wght@400;500;700&family=Open+Sans:wght@400;600&display=swap">
<style>
  :root {
    --backdrop: #e9e7e4;
    --card-white: #f7f7f7;
    --brand-blue: #1a6aa8;
    --name-blue: #0f5f99;
    --title-slate: #56708e;
    --text-grey: #555a60;
    --icon-blue: #1f5f95;
    --back-light: #0a73b4;
    --back-dark: #05426f;
    --white: #ffffff;
  }
  * { margin: 0; padding: 0; box-sizing: border-box; }
  html, body { width: 1200px; height: 960px; overflow: hidden; }
  body { background: var(--backdrop); position: relative; font-family: "Roboto", Arial, sans-serif; }

  .card { position: absolute; width: 600px; height: 344px; box-shadow: 0 3px 8px rgba(0,0,0,0.25); }
  .card-front { left: 315px; top: 113px; background: var(--card-white); }
  .card-back  { left: 311px; top: 472px; background: radial-gradient(ellipse at 45% 40%, var(--back-light) 0%, var(--back-dark) 85%); overflow: hidden; }

  .brand-square { position: absolute; left: 48px; top: 48px; width: 52px; height: 52px; background: var(--brand-blue); }
  .brand-divider { position: absolute; left: 115px; top: 39px; width: 2px; height: 96px; background: var(--brand-blue); }
  .brand-name { position: absolute; left: 125px; top: 50px; font-size: 40px; font-weight: 500; letter-spacing: 2px; color: var(--brand-blue); line-height: 1; }
  .brand-tagline { position: absolute; left: 126px; top: 102px; font-size: 15px; color: var(--brand-blue); font-family: "Open Sans", Arial, sans-serif; }

  .holder { position: absolute; right: 44px; top: 59px; text-align: right; }
  .holder-name { font-size: 20px; font-weight: 700; color: var(--name-blue); line-height: 24px; }
  .holder-title { font-size: 15px; font-weight: 500; color: var(--title-slate); line-height: 22px; }

  .contact-list { position: absolute; left: 43px; top: 230px; list-style: none; }
  .contact-list li { display: flex; align-items: center; height: 19px; font-size: 15px; color: var(--text-grey); }
  .contact-list svg { width: 13px; height: 13px; margin-right: 9px; fill: var(--icon-blue); }

  .address { position: absolute; right: 44px; top: 252px; text-align: right; font-size: 14.5px; line-height: 18.5px; color: var(--text-grey); }

  .back-name { position: absolute; left: 41px; top: 198px; font-size: 56px; font-weight: 500; letter-spacing: 3px; color: var(--white); line-height: 1; }
  .back-tagline { position: absolute; left: 43px; top: 264px; font-size: 21px; color: var(--white); font-family: "Open Sans", Arial, sans-serif; }
  .back-web { position: absolute; left: 45px; top: 295px; font-size: 14px; letter-spacing: 5.6px; color: var(--white); }
</style>
</head>
<body>
  <section class="card card-front">
    <div class="brand-square"></div>
    <div class="brand-divider"></div>
    <div class="brand-name">CALVORA</div>
    <div class="brand-tagline">BACK OFFICE SOLUTIONS</div>

    <div class="holder">
      <div class="holder-name">DANIEL REYES</div>
      <div class="holder-title">CEO/FOUNDER</div>
    </div>

    <ul class="contact-list">
      <li><svg viewBox="0 0 16 16" aria-hidden="true"><path d="M3.5 1l2.5 3-1.6 1.8c.9 2 2.6 3.8 4.8 4.8L11 9l3 2.5-1.5 3C6.5 14 2 9.5 1.5 2.5z"/></svg>555 214 7830</li>
      <li><svg viewBox="0 0 16 16" aria-hidden="true"><path d="M4.5 0h7a1 1 0 0 1 1 1v14a1 1 0 0 1-1 1h-7a1 1 0 0 1-1-1V1a1 1 0 0 1 1-1zm.7 2v10.5h5.6V2z"/></svg>555 386 1942</li>
      <li><svg viewBox="0 0 16 16" aria-hidden="true"><path d="M4 1h8v4H4zM1 6h14v7h-2v-3H3v3H1zM4 11h8v4H4z"/></svg>555 903 6217</li>
      <li><svg viewBox="0 0 16 16" aria-hidden="true"><path d="M1 3h14v10H1zm1.2 1.2L8 8.5l5.8-4.3z"/></svg>hello@calvora.com</li>
    </ul>

    <div class="address">
      1240 Harbor View Road<br>
      Juneau, Alaska 99801<br>
      www.calvora.com
    </div>
  </section>

  <section class="card card-back">
    <div class="back-name">CALVORA</div>
    <div class="back-tagline">BACK OFFICE SOLUTIONS</div>
    <div class="back-web">www.calvora.com</div>
  </section>
</body>
</html>
```